LumaPeak business card

We are a performing arts company providing training (to both kids and adults) as well as performers for events. We hope to bring joy and confidence on stage to the people we train, as well as joy to the audience when our artistes perform. Designs should convey the joy, confidence and vibrancy on stage. Design business card using the attached logo. Card to include name, mobile tel, email address, company address, and website. Double sided. To also include the following list of what the company does:
• Training & Enrichment
• Private & Corporate Entertainment
- Music composition & production

Industry/Entity Type

Training

Contact Information for Business Card

Card to include name, mobile tel, email address, company address, and website. Double sided. To also include the following list of what the company does:
• Training & Enrichment

Requirements
Nice to have
• Card need not be the traditional rectangular in shape but not too outrageous.

```html
<!DOCTYPE html>
<html lang="en">
<head>
<meta charset="utf-8">
<title>LumaPeak business card</title>
<link rel="stylesheet" href="https://fonts.googleapis.com/css2?family=Varela+Round&family=Nunito:wght@700;800&display=swap">
<style>
  :root {
    --backdrop: #2a2a2c;
    --card: #ffffff;
    --rim: #6cc6e8;
    --ring-text: #2a7fc9;
    --brand: #214f93;
    --brand-dot: #f2b51f;
    --tagline: #1f4a86;
    --name: #e5453a;
    --phone: #f29a1d;
    --email: #8cc63f;
    --address: #28b6cc;
    --web: #8e3a9e;
  }
  * { margin: 0; padding: 0; box-sizing: border-box; }
  html, body { width: 1200px; height: 800px; overflow: hidden; background: var(--backdrop); }
  .canvas {
    width: 1200px; height: 800px;
    display: flex; align-items: center; justify-content: center; gap: 60px;
  }
  .card-side { width: 520px; height: 520px; display: block; }
  .card-face { fill: var(--card); stroke: var(--rim); stroke-width: 12; }
  .brand-name { font-family: "Nunito", sans-serif; font-weight: 800; fill: var(--brand); }
  .brand-mark { fill: var(--brand-dot); }
  .tagline { font-family: "Nunito", sans-serif; font-weight: 700; fill: var(--tagline); }
  .service-ring { font-family: "Varela Round", sans-serif; font-size: 23px; fill: var(--ring-text); }
  .contact { font-family: "Varela Round", sans-serif; font-size: 23px; text-anchor: middle; }
  .contact-name { fill: var(--name); }
  .contact-phone { fill: var(--phone); }
  .contact-email { fill: var(--email); }
  .contact-address { fill: var(--address); }
  .contact-web { fill: var(--web); }
</style>
</head>
<body>
<main class="canvas">

  <!-- Front side -->
  <svg class="card-side card-front" viewBox="0 0 520 520" aria-label="LumaPeak card, front side">
    <circle class="card-face" cx="260" cy="260" r="250"/>
    <circle class="brand-mark" cx="260" cy="160" r="62"/>
    <text class="brand-name" x="260" y="325" font-size="82" text-anchor="middle">LumaPeak</text>
    <text class="tagline" x="260" y="378" font-size="33" text-anchor="middle">shining on every stage</text>
  </svg>

  <!-- Back side -->
  <svg class="card-side card-back" viewBox="0 0 520 520" aria-label="LumaPeak card, back side">
    <defs>
      <path id="ring-path" d="M 150 433.3 A 200 200 0 1 1 370 433.3 A 200 200 0 0 1 150 433.3"/>
    </defs>
    <circle class="card-face" cx="260" cy="260" r="250"/>
    <text class="service-ring">
      <textPath href="#ring-path" textLength="1200" lengthAdjust="spacing">Music composition &amp; production • Training &amp; Enrichment • Private &amp; Corporate Entertainment •</textPath>
    </text>

    <circle class="brand-mark" cx="260" cy="118" r="24"/>
    <text class="brand-name" x="260" y="190" font-size="40" text-anchor="middle">LumaPeak</text>
    <text class="tagline" x="260" y="216" font-size="15" text-anchor="middle">shining on every stage</text>

    <text class="contact contact-name" x="260" y="282">Mara LENTZ</text>
    <text class="contact contact-phone" x="260" y="316">(214) 555 380 917</text>
    <text class="contact contact-email" x="260" y="350">contact@lumapeak.com</text>
    <text class="contact contact-address" x="260" y="384">1180 West Harbor Lane</text>
    <text class="contact contact-web" x="260" y="418">www.LumaPeak.com</text>
  </svg>

</main>
</body>
</html>
```